Business Name is RT Glamworks - Make-up Artist

I'm looking for an attractive and eye catching business card for for mobile make-up artist business. On the front of the card, I just want the name RT Glamworks in feminine type cursive writing and underneath my name Tessa Rowan and Make-Up Artist.
On the back of the card, I would like written down one side the following;
Make-Up Tutorials
Bridal
Photography
Debutante
Formals
Family Portraits
I would also like the following details as well as the Chatterly and Picvault Icons;
Mobile: 0482 615 379
Email: tessarowan@mailbrook.net
Website: tessarowan.velmira.com
Certificate III in Make-Up
Also, I would like a section that says Your Next Appointment and a space to put that information.
I would also like the Velmira Symbol on the bottom right hand corner (I have attached)

Target Market(s)

Mostly females

Industry/Entity Type

Makeup

Contact Information for Business Card

RT Glamworks
Tessa Rowan - Make-Up Artist

Font styles to use
Script

Colors
b768aa
886aae
e34297

Requirements
Must have
• Mobile: 0482 615 379
• Email: tessarowan@mailbrook.net
• Website: tessarowan.velmira.com
• Certificate III in Make-Up
Nice to have
• Something to do with make-up like a smudged lipstick or some eye shadow
Should not have
• Don't want it too busy

```html
<!DOCTYPE html>
<html lang="en">
<head>
<meta charset="utf-8">
<title>RT Glamworks – Business Card</title>
<link rel="stylesheet" href="https://fonts.googleapis.com/css2?family=Caveat+Brush&family=Cormorant+Garamond:wght@500&family=Open+Sans:wght@400;600;700&family=Open+Sans+Condensed:wght@700&display=swap">
<style>
  :root {
    --mauve: #b768aa;
    --violet: #886aae;
    --pink: #e34297;
    --charcoal: #333335;
    --paper: #ffffff;
    --backdrop: #ecebe8;
    --leaf: #4f8a3c;
    --line: #9a86bd;
    --kiss-light: #f2b6c9;
    --kiss-deep: #d97b8c;
  }
  * { box-sizing: border-box; margin: 0; padding: 0; }
  html, body { width: 1200px; height: 1200px; overflow: hidden; }
  body {
    background: var(--backdrop);
    font-family: "Open Sans", Arial, sans-serif;
    position: relative;
  }
  .card {
    position: absolute;
    left: 160px;
    width: 880px;
    height: 500px;
    overflow: hidden;
    box-shadow: 0 6px 18px rgba(0,0,0,0.12);
  }
  .card--front { top: 70px; background: var(--charcoal); }
  .card--back { top: 630px; background: var(--paper); }

  .colour-band {
    position: absolute; left: 0; bottom: 0;
    width: 100%; height: 40px; display: flex;
  }
  .colour-band span { flex: 1; height: 100%; }
  .colour-band .band-pink { background: var(--pink); }
  .colour-band .band-violet { background: var(--violet); }
  .colour-band .band-mauve { background: var(--mauve); }

  /* front */
  .brand-block {
    position: absolute; left: 0; right: 0; top: 120px;
    text-align: center;
  }
  .brand-name {
    font-family: "Caveat Brush", cursive;
    font-size: 112px; line-height: 1;
    color: var(--mauve);
    letter-spacing: 4px;
    transform: rotate(-2deg);
  }
  .owner-name {
    font-family: "Cormorant Garamond", serif;
    font-size: 44px; color: #fff;
    letter-spacing: 9px; margin-top: 6px;
  }
  .owner-role {
    font-family: "Open Sans", sans-serif;
    font-weight: 700; font-size: 19px;
    color: var(--pink); letter-spacing: 2px;
    margin-top: 2px; padding-left: 180px;
  }

  /* back */
  .service-list {
    position: absolute; left: 40px; top: 34px;
    font-size: 19px; color: var(--violet); letter-spacing: .3px;
  }
  .qualification {
    position: absolute; left: 330px; top: 68px;
    font-size: 24px; color: var(--pink);
  }
  .lipstick-art {
    position: absolute; left: 150px; top: 130px;
    width: 320px; height: 200px; border-radius: 50%;
    background: radial-gradient(ellipse at 60% 50%, var(--kiss-deep) 0%, var(--kiss-light) 55%, rgba(255,255,255,0) 72%);
  }
  .contact-list {
    position: absolute; left: 40px; top: 345px;
    list-style: none; font-size: 20px; color: var(--violet);
  }
  .contact-list li { display: flex; align-items: center; gap: 10px; height: 30px; }
  .contact-list svg { width: 20px; height: 20px; flex: none; }

  .appointment {
    position: absolute; left: 510px; top: 112px; width: 330px;
    color: var(--violet);
  }
  .appointment h2 {
    font-family: "Open Sans Condensed", "Open Sans", sans-serif;
    font-weight: 700; font-size: 26px; letter-spacing: .5px;
  }
  .field-row { display: flex; gap: 14px; margin-top: 20px; font-size: 17px; }
  .field { display: flex; flex: 1; align-items: flex-end; gap: 6px; }
  .field i { flex: 1; border-bottom: 1.5px solid var(--line); height: 18px; }
  .day-grid { margin-top: 22px; font-size: 17px; }
  .day-row { display: flex; gap: 10px; margin-bottom: 12px; }
  .day { display: flex; align-items: center; gap: 5px; }
  .day i { width: 20px; height: 20px; border: 1.8px solid var(--pink); border-radius: 50%; }

  .partner-mark {
    position: absolute; right: 40px; bottom: 70px;
    display: flex; flex-direction: column; align-items: center; gap: 8px;
    color: var(--leaf);
  }
  .partner-mark .dot { width: 58px; height: 58px; border-radius: 50%; background: var(--leaf); }
  .partner-mark span { font-family: "Open Sans", sans-serif; font-weight: 600; font-size: 18px; letter-spacing: 2px; }

  .social-names {
    position: absolute; left: 333px; bottom: 0; height: 40px;
    display: flex; align-items: center; gap: 18px;
    font-size: 15px; font-weight: 600; color: #fff;
  }
</style>
</head>
<body>

<section class="card card--front" aria-label="Card front">
  <div class="brand-block">
    <h1 class="brand-name">RT GLAMWORKS</h1>
    <p class="owner-name">TESSA ROWAN</p>
    <p class="owner-role">Make-Up Artist</p>
  </div>
  <div class="colour-band"><span class="band-pink"></span><span class="band-violet"></span><span class="band-mauve"></span></div>
</section>

<section class="card card--back" aria-label="Card back">
  <p class="service-list">Make-Up Tutorials-Bridal-Photography-Debutante-Formals-Family Portraits</p>
  <p class="qualification">Certificate III in Make-Up</p>

  <div class="lipstick-art" role="img" aria-label="Smudged pink lipstick kiss prints"></div>

  <ul class="contact-list">
    <li>
      <svg viewBox="0 0 20 20" aria-hidden="true"><path d="M5 2l3 4-2 2c1 2 3 4 5 5l2-2 4 3-2 3C9 17 3 11 2 5z" fill="var(--pink)"/></svg>
      0482 615 379
    </li>
    <li>
      <svg viewBox="0 0 20 20" aria-hidden="true"><rect x="1" y="4" width="18" height="12" fill="var(--pink)"/><path d="M1 4l9 7 9-7" stroke="#fff" stroke-width="1.5" fill="none"/></svg>
      tessarowan@mailbrook.net
    </li>
    <li>
      <svg viewBox="0 0 20 20" aria-hidden="true"><circle cx="10" cy="10" r="9" fill="var(--pink)"/><ellipse cx="10" cy="10" rx="4" ry="9" stroke="#fff" stroke-width="1.3" fill="none"/><path d="M1 10h18" stroke="#fff" stroke-width="1.3"/></svg>
      tessarowan.velmira.com
    </li>
  </ul>

  <div class="appointment">
    <h2>NEXT APPOINTMENT</h2>
    <div class="field-row"><span class="field">Name: <i></i></span></div>
    <div class="field-row">
      <span class="field">Date: <i></i></span>
      <span class="field">Time: <i></i></span>
    </div>
    <div class="day-grid">
      <div class="day-row">
        <span class="day">Mon <i></i></span><span class="day">Tue <i></i></span>
        <span class="day">Wed <i></i></span><span class="day">Thur <i></i></span>
      </div>
      <div class="day-row">
        <span class="day">Fri <i></i></span><span class="day">Sat <i></i></span>
      </div>
    </div>
  </div>

  <div class="partner-mark"><i class="dot"></i><span>VELMIRA</span></div>

  <div class="colour-band"><span class="band-pink"></span><span class="band-violet"></span><span class="band-mauve"></span></div>
  <div class="social-names"><span>Picvault</span><span>Chatterly</span></div>
</section>

</body>
</html>
```